VentriLedger.Com PowerPoint

I need a PowerPoint layout for my presentations. My business is called VentriLedger.Com - my presentations teach cardiologists how to document their procedures and visits and teaches them how to bill accurately for them.

Industry/Entity Type

Business

Requirements
Must have
• the logo should be subtly there on each page - perhaps as a watermark? I'm really not creative; please help.

```html
<!DOCTYPE html>
<html lang="en">
<head>
<meta charset="utf-8">
<title>VentriLedger.com Presentation Template</title>
<link href="https://fonts.googleapis.com/css2?family=Raleway:wght@300;400;600;700&family=Roboto:wght@400;500;700&family=Roboto+Condensed:wght@400;700&display=swap" rel="stylesheet">
<style>
:root{
  --canvas:#e4e5e7;
  --paper:#f7f7f7;
  --white:#ffffff;
  --ink:#3c3c3e;
  --ink-soft:#555557;
  --muted:#8a8a8c;
  --red:#d71f2b;
  --line:#e2e2e2;
  --row-dark:#424244;
  --blue:#0aa0d8;
  --purple:#9b4db5;
  --orange:#e46f32;
  --green:#7cc242;
}
*{box-sizing:border-box;margin:0;padding:0}
html,body{width:1064px;height:1200px;overflow:hidden;background:var(--canvas)}
body{position:relative;font-family:"Roboto",Arial,sans-serif;color:var(--ink)}
.slide{position:absolute;width:582px;height:436px;transform:scale(0.8866);transform-origin:0 0;overflow:hidden;background:var(--paper)}
.c1{left:12px}.c2{left:536px}
.r1{top:9px}.r2{top:407px}.r3{top:805px}
.brand{position:absolute;display:flex;align-items:center;gap:12px;font-family:"Raleway",sans-serif;font-weight:400;letter-spacing:1px;color:var(--ink)}
.brand .dot{width:44px;height:44px;border-radius:50%;background:var(--red)}
.brand-lg{font-size:36px}
.brand.on-dark{color:var(--white)}
.pres-title{position:absolute;right:22px;top:295px;text-align:right;font-family:"Raleway",sans-serif;font-weight:300;font-size:28px;color:var(--ink-soft);line-height:1}
.pres-title span{display:block;font-size:13px;color:var(--red);font-weight:400;margin-top:2px}
.band{position:absolute;left:0;right:0;bottom:0;height:71px;background:var(--ink)}
.band .label{position:absolute;left:11px;top:18px;font-family:"Raleway",sans-serif;font-size:20px;color:var(--white);letter-spacing:.5px;line-height:1}
.band .label b{font-weight:700}
.band .label small{display:block;font-size:14px;color:var(--red);margin-top:2px;letter-spacing:0}
.band .tile{position:absolute;left:501px;top:13px;width:66px;height:48px;background:#464648}
.band .tile i{position:absolute;left:23px;top:14px;width:20px;height:20px;border:1.5px solid var(--red)}
.head{position:absolute;left:0;right:0;top:0;height:53px;background:var(--white);border-bottom:1px solid var(--line);text-align:center}
.head h2{font-family:"Raleway",sans-serif;font-weight:400;font-size:28px;color:var(--red);letter-spacing:.5px;margin-top:2px;line-height:34px}
.head p{font-family:"Raleway",sans-serif;font-size:10px;color:var(--muted);letter-spacing:.5px}
.head p b{font-weight:700}
.foot{position:absolute;left:0;right:0;bottom:0;height:36px;background:var(--ink);display:flex;align-items:center;padding-left:12px;font-size:11px;color:var(--white)}
.foot .mini{font-family:"Raleway",sans-serif;font-size:9px;letter-spacing:.5px;width:106px}
.foot b{font-weight:700}
.foot .to{color:var(--red);margin-left:3px}
.foot .num{position:absolute;right:12px;color:var(--red);font-size:8px}
.photo{position:absolute;left:38px;top:79px;width:505px;height:224px;background:#e4e4e4;border:1px solid #e9b9bd}
.notes{position:absolute;left:38px;width:505px;display:flex;gap:12px;font-size:8.5px;line-height:1.3;color:var(--ink-soft)}
.notes i{flex:none;width:14px;height:14px;border:2px solid var(--red);border-radius:50%;margin-top:1px}
.tbl-title{position:absolute;top:73px;font-size:17px;color:var(--ink);display:flex;align-items:center;gap:6px;font-family:"Roboto Condensed",sans-serif}
.tbl-title b{font-weight:700}
.tbl-title i{width:17px;height:14px;border:2px solid var(--red);background:linear-gradient(var(--red),var(--red)) 0 4px/100% 1.5px no-repeat,linear-gradient(90deg,transparent 5px,var(--red) 5px,var(--red) 6.5px,transparent 6.5px) }
table{position:absolute;top:103px;width:260px;border-collapse:collapse;font-family:"Roboto Condensed",sans-serif;font-size:6.5px;color:var(--ink)}
th{height:23px;font-size:9px;font-weight:400;color:var(--white);background:var(--ink);text-align:center}
td{height:25.2px;border-bottom:1px solid var(--line);background:var(--white);text-align:center;padding:0 3px}
td:first-child{color:var(--red);font-size:9px;width:36px}
td:nth-child(2){text-align:left;width:97px}
.dark th{background:var(--red);font-weight:700}
.dark td{background:var(--row-dark);color:#e6e6e6;border-bottom-color:#505052}
.more{position:absolute;top:356px;width:260px;height:24px;background:var(--red);color:var(--white);font-size:10px;font-weight:500;display:flex;align-items:center;justify-content:center}
.more.grey{background:#a0a0a2}
.g-title{position:absolute;top:78px;font-family:"Roboto Condensed",sans-serif;font-size:17px;color:var(--ink)}
.g-title b{font-weight:700}
.chart{position:absolute;left:0;top:0}
.gnotes{position:absolute;width:215px;font-size:7.2px;line-height:1.3;color:var(--ink-soft)}
.gnotes p{position:relative;padding-left:14px;margin-bottom:11px}
.gnotes p::before{content:"";position:absolute;left:0;top:2px;border-left:4px solid var(--red);border-top:3px solid transparent;border-bottom:3px solid transparent}
.dark-slide{background:var(--ink)}
.contact{position:absolute;left:15px;font-size:8px;line-height:1.2;color:var(--white)}
.contact h4{color:var(--red);font-size:9.5px;font-weight:400}
.web{position:absolute;right:70px;bottom:17px;font-size:9px;color:var(--red)}
</style>
</head>
<body>

<section class="slide c1 r1">
  <div class="brand brand-lg" style="left:128px;top:178px"><span class="dot"></span>VentriLedger.com</div>
</section>

<section class="slide c2 r1">
  <div class="brand brand-lg" style="left:128px;top:150px"><span class="dot"></span>VentriLedger.com</div>
  <div class="pres-title">Presentation Title<span>JAN 2014</span></div>
  <div class="band">
    <div class="label"><b>COMPANY</b> PRESENTATION<small>to <b>Business</b>/Client</small></div>
    <div class="tile"><i></i></div>
  </div>
</section>

<section class="slide c1 r2">
  <header class="head"><h2>IMAGE IN LANDSCAPE VIEW</h2><p>WITH COMPLETELY <b>CUSTOMIZABLE</b> ICONS</p></header>
  <div class="photo" role="img" aria-label="Landscape photo placeholder"></div>
  <div class="notes" style="top:318px"><i></i><p><b>Aenean</b> ridiculus tortor quis interdum id habitant ad, natoque consectetuer nisl auctor libero quisque euismod ante inceptos malesuada ligula mattis.</p></div>
  <div class="notes" style="top:353px"><i></i><p><b>Aenean</b> ridiculus tortor quis interdum id habitant ad, natoque consectetuer nisl auctor libero quisque euismod ante inceptos malesuada ligula mattis.</p></div>
  <footer class="foot"><span class="mini">VentriLedger.com</span><b>COMPANY</b>&nbsp;PRESENTATION<span class="to">to <b>Business</b>/client</span><span class="num">3</span></footer>
</section>

<section class="slide c2 r2">
  <header class="head"><h2>COLOR STYLE TABLES</h2><p>CHOOSE FROM A <b>LIGHT</b> OR <b>DARK</b> THEME</p></header>
  <div class="tbl-title" style="left:23px"><i></i><span><b>Light</b> Theme</span></div>
  <table style="left:21px">
    <tr><th>Item</th><th>Step/Action</th><th>Responsible</th><th>Target Date</th></tr>
    <tr><td>1</td><td>Business X, Y, Z high level needs</td><td>Business X, Y, Z</td><td>5/24/2013</td></tr>
    <tr><td>2</td><td>Understand current situation and safety mana</td><td>Business X, Y, Z</td><td>5/31/2013</td></tr>
    <tr><td>3</td><td>Submit Proposal</td><td>Business X, Y, Z</td><td>6/3/2013</td></tr>
    <tr><td>4</td><td>Review Proposal</td><td>Business X, Y, Z</td><td>TBD</td></tr>
    <tr><td>5</td><td>Prepare Final Proposal &amp; Statement of Work (SOW)</td><td>Business X, Y, Z</td><td>TBD</td></tr>
    <tr><td>6</td><td>Complete and sign SOW</td><td>Business X, Y, Z</td><td>TBD</td></tr>
    <tr><td>7</td><td>Schedule project start date</td><td>Business X, Y, Z</td><td>TBD</td></tr>
    <tr><td>8</td><td>Kick-off Project</td><td>Business X, Y, Z</td><td>TBD</td></tr>
    <tr><td>9</td><td>Complete Project</td><td>Business X, Y, Z</td><td>TBD</td></tr>
  </table>
  <div class="more" style="left:21px">• Additional Information</div>
  <div class="tbl-title" style="left:301px"><i></i><span><b>Dark</b> Theme</span></div>
  <table class="dark" style="left:301px">
    <tr><th>Item</th><th>Step/Action</th><th>Responsible</th><th>Target Date</th></tr>
    <tr><td>1</td><td>Business X, Y, Z high level needs</td><td>Business X, Y, Z</td><td>5/24/2013</td></tr>
    <tr><td>2</td><td>Understand current situation and safety mana</td><td>Business X, Y, Z</td><td>5/31/2013</td></tr>
    <tr><td>3</td><td>Submit Proposal</td><td>Business X, Y, Z</td><td>6/3/2013</td></tr>
    <tr><td>4</td><td>Review Proposal</td><td>Business X, Y, Z</td><td>TBD</td></tr>
    <tr><td>5</td><td>Prepare Final Proposal &amp; Statement of Work (SOW)</td><td>Business X, Y, Z</td><td>TBD</td></tr>
    <tr><td>6</td><td>Complete and sign SOW</td><td>Business X, Y, Z</td><td>TBD</td></tr>
    <tr><td>7</td><td>Schedule project start date</td><td>Business X, Y, Z</td><td>TBD</td></tr>
    <tr><td>8</td><td>Kick-off Project</td><td>Business X, Y, Z</td><td>TBD</td></tr>
    <tr><td>9</td><td>Complete Project</td><td>Business X, Y, Z</td><td>TBD</td></tr>
  </table>
  <div class="more grey" style="left:301px">• Additional Information</div>
  <footer class="foot"><span class="mini">VentriLedger.com</span><b>COMPANY</b>&nbsp;PRESENTATION<span class="to">to <b>Business</b>/client</span><span class="num">5</span></footer>
</section>

<section class="slide c1 r3">
  <header class="head"><h2>COLOR STYLE GRAPHS</h2><p>CHOOSE TO USE BETWEEN <b>MAIN</b> AND <b>SECONDARY</b> COLOR THEMES</p></header>
  <div class="g-title" style="left:28px"><b>Graph</b> Main Colors</div>
  <div class="g-title" style="left:330px"><b>Graph</b> Secondary Colors</div>
  <svg class="chart" width="582" height="436" viewBox="0 0 582 436" font-family="Roboto, sans-serif" font-size="7" fill="#3c3c3e">
    <g stroke="#e6e6e6" stroke-width="1">
      <line x1="48" y1="119" x2="264" y2="119"/><line x1="48" y1="161" x2="264" y2="161"/>
      <line x1="48" y1="203" x2="264" y2="203"/><line x1="48" y1="245" x2="264" y2="245"/>
    </g>
    <text x="28" y="122">100</text><text x="32" y="164">75</text><text x="32" y="206">50</text><text x="32" y="248">25</text><text x="36" y="289">0</text>
    <polygon points="48,196 119,214 191,170 263,182 263,287 48,287" fill="#3c3c3e"/>
    <polygon points="48,237 119,248 119,287 48,287" fill="#a3a3a5"/>
    <polygon points="48,262 119,245 191,195 263,124 263,287 48,287" fill="#d71f2b"/>
    <line x1="48" y1="287" x2="264" y2="287" stroke="#3c3c3e" stroke-width="1"/>
    <text x="40" y="296">2007</text><text x="112" y="296">2008</text><text x="184" y="296">2009</text><text x="255" y="296">2010</text>
    <g stroke="#ffffff" stroke-width="2">
      <path d="M418,202 L383,290.3 A95,95 0 0 1 447.4,111.7 Z" fill="#0aa0d8"/>
      <path d="M418,202 L511.3,219.8 A95,95 0 0 1 383,290.3 Z" fill="#9b4db5"/>
      <path d="M418,202 L491.2,141.4 A95,95 0 0 1 511.3,219.8 Z" fill="#e46f32"/>
      <path d="M423.6,193.7 L453,103.4 A95,95 0 0 1 496.8,133.1 Z" fill="#7cc242"/>
    </g>
    <g fill="#ffffff" font-size="10">
      <text x="368" y="181">50%</text><text x="468" y="152">9%</text><text x="472" y="202">14%</text><text x="429" y="266">28%</text>
    </g>
    <g font-size="7">
      <circle cx="520" cy="257" r="3.5" fill="#7cc242"/><text x="529" y="260">2007</text>
      <circle cx="520" cy="267" r="3.5" fill="#e46f32"/><text x="529" y="270">2008</text>
      <circle cx="520" cy="278" r="3.5" fill="#9b4db5"/><text x="529" y="281">2009</text>
      <circle cx="520" cy="289" r="3.5" fill="#0aa0d8"/><text x="529" y="292">2010</text>
    </g>
  </svg>
  <div class="gnotes" style="left:40px;top:311px">
    <p><b>Aenean</b> ridiculus tortor quis interdum id habitant ad, natoque consectetuer nisl auctor libero quisque euismod ante inceptos malesuada ligula mattis.</p>
    <p>Varius inceptos <b>nascetur</b> mollis dui aptent ultrices. Pretium pulvinar ante lobortis convallis lectus netus vitae penatibus eros at blandit. Parturient.</p>
  </div>
  <div class="gnotes" style="left:325px;top:311px">
    <p><b>Aenean</b> ridiculus tortor quis interdum id habitant ad, natoque consectetuer nisl auctor libero quisque euismod ante inceptos malesuada ligula mattis.</p>
    <p>Varius inceptos <b>nascetur</b> mollis dui aptent ultrices. Pretium pulvinar ante lobortis convallis lectus netus vitae penatibus eros at blandit. Parturient.</p>
  </div>
  <footer class="foot"><span class="mini">VentriLedger.com</span><b>COMPANY</b>&nbsp;PRESENTATION<span class="to">to <b>Business</b>/client</span><span class="num">7</span></footer>
</section>

<section class="slide c2 r3 dark-slide">
  <div class="brand brand-lg on-dark" style="left:128px;top:185px"><span class="dot"></span>VentriLedger.com</div>
  <div class="contact" style="top:345px"><h4>Contact us:</h4>555-014-2290<br>info@ventriledger.com</div>
  <div class="contact" style="top:390px"><h4>Central Office:</h4>Address Line 1<br>Address Line 2</div>
  <div class="web">www.ventriledger.com</div>
</section>

</body>
</html>
```